Signal Post Hire Banner Ad Design Project

Hello Sketch Hive,

We are looking for a banner ad that we can email to general contractors, and consulting firms in our service area to make them aware of our service.

We are an electrical contracting company based in Toronto, Ontario, Canada and one of divisions rents traffic light systems. We install our portable systems mainly in underground parking garages when construction restricts two way traffic to one lane. Our systems also get installed on ramps, and other areas that are under construction. Essentially, they allow phasing of big construction projects so the disruptions of traffic flow is kept to a minimal.
Our systems differ from other companies' rentals because our systems are cheaper, more reliable since they aren't wireless and they are LED (no bulbs burning out), we provide countdown lights that increase the effectiveness of the system and motorists' patience, and our systems adapt to rush hour traffic flow patterns at each site.
We have installed the systems at high profile locations throughout the city including The Marlowe Quay Arcade, and Brinwick Plaza.
We can provide job specific pricing or a monthly rate both of which include installation and removal.

I don't have very many good images of our systems but maybe you can photoshop our systems into another photo or a stock image might work as well.

More information on our systems can be found at www.corvanpower.example
Updates

Project Deadline Extended
Reason: Hi everyone, I am extending the deadline for submissions because I haven't had a proper chance to provide feedback to some of the designers who have submitted banner ads. I know it is frustrating when the deadline gets extended and I apologize. Thank you again and if I haven't provided feedback to you yet, please be patient because there have been some excellent designs that have been submitted so far. Dale

Project Deadline Extended
Reason: Still working with designers towards the right design.

Project Deadline Extended
Reason: I have been swamped with work and haven't been able to provide proper feedback to designers. Thanks for your patience, Dale

Industry/Entity Type

Construction

Requirements
Must have
• Corvan Power Logo

Focus on the fact that our systems are lower in price than our competitors or the fact that they are more cost effective.

Something that touches on the fact that our systems have countdown lights and adaptive control which increases traffic flow. This is a unique feature that no other company has.

```html
<!DOCTYPE html>
<html lang="en">
<head>
<meta charset="utf-8">
<title>Corvan Power – Signal Post Hire Banner</title>
<link rel="stylesheet" href="https://fonts.googleapis.com/css2?family=Arimo:wght@400;700&display=swap">
<style>
  :root {
    --flag-red: #c8625e;
    --flag-red-soft: #dca3a0;
    --flag-white: #f1eeee;
    --panel-grey-light: #d9d9d9;
    --panel-grey-dark: #a9a9a9;
    --light-housing: #3a3a3a;
    --badge-orange: #f08a1c;
    --badge-orange-light: #ffc15a;
    --badge-text: #5a2a00;
    --tag-bg: #8a5a58;
    --tag-text: #ffffff;
    --glow-blue: #2a4cff;
    --logo-ink: #111111;
  }
  html, body {
    margin: 0;
    padding: 0;
    overflow: hidden;
    background: #ffffff;
  }
  .banner {
    position: relative;
    width: 1200px;
    height: 148px;
    overflow: hidden;
    font-family: "Arimo", Arial, sans-serif;
    background: var(--flag-white);
  }
  .side-panel {
    position: absolute;
    top: 0;
    height: 148px;
    background: linear-gradient(180deg, var(--panel-grey-light), var(--panel-grey-dark));
  }
  .side-panel--left { left: 0; width: 302px; }
  .side-panel--right { left: 898px; width: 302px; }
  .flag-band {
    position: absolute;
    top: 0;
    height: 148px;
    background: var(--flag-red);
  }
  .flag-band--left { left: 302px; width: 128px; }
  .flag-band--right { left: 775px; width: 123px; }
  .flag-emblem {
    position: absolute;
    left: 520px;
    top: 20px;
    width: 165px;
    height: 108px;
    background: linear-gradient(180deg, var(--flag-red-soft), var(--flag-white));
  }
  .signal-unit {
    position: absolute;
    left: 0;
    top: 0;
    width: 38px;
    height: 148px;
    background: linear-gradient(90deg, #555, var(--light-housing) 60%, #222);
  }
  .new-badge {
    position: absolute;
    left: 160px;
    top: 4px;
    width: 104px;
    height: 104px;
  }
  .new-badge text {
    font-family: "Arimo", Arial, sans-serif;
    font-weight: 700;
    font-size: 22px;
    fill: var(--badge-text);
  }
  .price-tag {
    position: absolute;
    left: 466px;
    top: 62px;
    width: 276px;
    height: 29px;
    line-height: 29px;
    text-align: center;
    background: var(--tag-bg);
    color: var(--tag-text);
    font-size: 17px;
    border-radius: 3px;
  }
  .feature-line {
    position: absolute;
    left: 306px;
    top: 127px;
    margin: 0;
    font-size: 20px;
    line-height: 24px;
    color: #ffffff;
    white-space: nowrap;
    text-shadow: 0 0 2px var(--glow-blue), 0 0 3px var(--glow-blue), 0 0 4px var(--glow-blue);
  }
  .brand {
    position: absolute;
    left: 872px;
    top: 80px;
    display: flex;
    align-items: center;
    gap: 10px;
  }
  .brand__mark {
    width: 18px;
    height: 18px;
    background: var(--logo-ink);
  }
  .brand__name {
    font-size: 40px;
    line-height: 44px;
    font-weight: 700;
    color: var(--logo-ink);
  }
</style>
</head>
<body>
  <div class="banner">
    <div class="side-panel side-panel--left"></div>
    <div class="flag-band flag-band--left"></div>
    <div class="flag-band flag-band--right"></div>
    <div class="side-panel side-panel--right"></div>
    <div class="flag-emblem" role="img" aria-label="National flag emblem at the centre of the flag"></div>

    <div class="signal-unit" role="img" aria-label="Portable traffic light with red, amber and green lamps"></div>

    <svg class="new-badge" viewBox="0 0 104 104" aria-label="New">
      <defs>
        <radialGradient id="badgeFill" cx="50%" cy="40%" r="60%">
          <stop offset="0%" stop-color="#ffc15a"/>
          <stop offset="100%" stop-color="#f08a1c"/>
        </radialGradient>
      </defs>
      <polygon fill="url(#badgeFill)" stroke="#ffffff" stroke-width="3"
        points="52,4 60,20 76,10 76,28 95,28 86,44 100,54 84,62 92,80 74,78 70,96 56,84 44,98 38,80 20,88 22,70 4,64 18,52 6,38 24,34 22,16 40,22"/>
      <text x="52" y="60" text-anchor="middle" transform="rotate(-15 52 56)">NEW</text>
    </svg>

    <div class="price-tag">Best System in Lower Price</div>

    <div class="brand">
      <span class="brand__mark"></span>
      <span class="brand__name">Corvan Power</span>
    </div>

    <p class="feature-line">Countdown Lights And Adaptive Control which increases traffic</p>
  </div>
</body>
</html>
```